Modern claims management company

We need a new company presentation brochure, composed of about 20 pages in A4 format.
Cover, page 1 who we are, page 2 company profile, page 3 territorial operation, page from 4 to 10 services offered and description of services (The title of the page are: Perizie e Liquidazione danni, riparazioni e sostituzioni, teleclaimer, accertamento danni da fenomeno elettrico, TPA, Auditing, drone pilot, Valutazione rischi), from 11 to 17 specializations (Sinistri gravi, R.C., Tecnologici, Energie rinnovabili, strutture, ambiente) page 18 e 19 integrated services (perdite occulte, ricerca guasti, indagini termografiche, crisis management), page 20 clients ( list companies and logos) page 21 contact.
The company is made up of various companies, which belong to the principal, each of which deals with specific activities.
To date we already have various logos of the main company (Tavesi and Durando) as well as the logos of the other companies. I load them on the portal.
Found then the graphic solution that we like we will have to proceed to make a presentation in similar powerpoint and the website.

Target Market(s)

Insurance Company, Insurance Broker

Other font styles liked:
• ARIAL

Colors
333333
5c5c5c
959595
0392cd

Requirements
Must have
• It must be clear, professional and modern.
Nice to have
• I indicate some competitor sites, so that you can better understand what we are doing. www.fenwoodhale.com, www.harrowpikestead.com, www.orsavantini.com, www.gruppotessandi.com, www.vandrini.eu.

```html
<!DOCTYPE html>
<html lang="en">
<head>
<meta charset="utf-8">
<title>Tavesi and Durando – Claims Management Brochure</title>
<link rel="stylesheet" href="https://fonts.googleapis.com/css2?family=Arimo:ital,wght@0,400;0,700;1,700&display=swap">
<style>
  :root {
    --ink: #333333;
    --grey-mid: #5c5c5c;
    --grey-light: #959595;
    --blue: #0392cd;
    --paper: #f1f1f1;
    --dark-panel: #4b4b4b;
    --backdrop: #d6d6d6;
  }
  * { box-sizing: border-box; margin: 0; padding: 0; }
  html, body { width: 841px; height: 1200px; overflow: hidden; }
  body {
    background: var(--backdrop);
    font-family: "Arimo", Arial, sans-serif;
    color: var(--ink);
    display: flex;
    flex-direction: column;
    justify-content: space-evenly;
    align-items: center;
  }
  .spread { display: flex; width: 780px; height: 552px; box-shadow: 0 6px 18px rgba(0,0,0,.18); }
  .page { position: relative; width: 390px; height: 552px; overflow: hidden; background: var(--paper); }
  .page > svg { position: absolute; inset: 0; width: 100%; height: 100%; }
  .abs { position: absolute; }

  /* company name */
  .brand-name { color: var(--ink); font-weight: 400; white-space: nowrap; }

  /* back cover */
  .back-cover { background: var(--dark-panel); }
  .logo-disc { left: 82px; top: 182px; width: 136px; height: 136px; display: flex; align-items: center; justify-content: center; }
  .logo-disc .brand-name { font-size: 13px; }
  .contact { left: 92px; top: 330px; color: #fff; font-size: 9px; line-height: 1.55; }
  .contact .phone { font-weight: 700; font-size: 11px; }
  .website { left: 40px; top: 500px; color: #fff; font-weight: 700; font-size: 13px; }

  /* front cover */
  .cover-brand { right: 24px; top: 46px; }
  .cover-brand .brand-name { font-size: 24px; }
  .cover-title { left: 104px; top: 348px; font-weight: 700; font-size: 28px; line-height: 1.02; text-transform: uppercase; }
  .cover-title .accent { color: var(--blue); }
  .cover-title .dark { color: var(--ink); }
  .cover-strap { left: 40px; top: 474px; width: 320px; color: #fff; font-size: 10.5px; line-height: 1.4; }

  /* inner pages */
  .section-head { font-weight: 700; font-style: italic; color: var(--blue); font-size: 14px; text-transform: uppercase; }
  .body-copy { font-size: 7.6px; line-height: 1.5; text-align: justify; }
  .who-head { left: 38px; top: 34px; }
  .who-copy-1 { left: 38px; top: 58px; width: 270px; }
  .who-copy-2 { left: 38px; top: 116px; width: 270px; }
  .profile-title { right: 22px; top: 120px; font-weight: 700; font-size: 21px; line-height: 1; text-align: right; color: var(--ink); text-transform: uppercase; }
  .profile-copy { left: 24px; top: 258px; width: 168px; color: #fff; }
  .why-head { left: 28px; top: 418px; color: #fff; font-style: normal; font-size: 16px; }
  .why-copy { left: 28px; top: 442px; width: 336px; color: #fff; }
</style>
</head>
<body>

<section class="spread cover-spread">
  <article class="page back-cover">
    <svg viewBox="0 0 390 552" aria-hidden="true">
      <defs>
        <linearGradient id="officeTeam" x1="0" y1="0" x2="1" y2="1">
          <stop offset="0" stop-color="#3f5f8f"/>
          <stop offset=".5" stop-color="#a9b8c8"/>
          <stop offset="1" stop-color="#d9c2b0"/>
        </linearGradient>
      </defs>
      <path d="M0 0 H390 V228 Q260 270 120 200 Q50 168 0 178 Z" fill="url(#officeTeam)" role="img" aria-label="Photo: colleagues reviewing documents at an office desk"/>
      <path d="M0 178 Q50 168 120 200 Q260 270 390 228" fill="none" stroke="var(--blue)" stroke-width="5"/>
      <circle cx="150" cy="250" r="74" fill="#fff" stroke="var(--blue)" stroke-width="5"/>
      <path d="M0 448 Q190 418 390 468" fill="none" stroke="#fff" stroke-width="3"/>
      <path d="M0 456 Q190 428 390 478 V552 H0 Z" fill="var(--blue)"/>
    </svg>
    <div class="abs logo-disc"><span class="brand-name">Tavesi and Durando</span></div>
    <div class="abs contact">
      <div class="phone">0000 111 222 333</div>
      <div>Your Address Here</div>
      <div>youremail@here.com</div>
    </div>
    <div class="abs website">www.yourwebsitehere.com</div>
  </article>

  <article class="page front-cover">
    <svg viewBox="0 0 390 552" aria-hidden="true">
      <defs>
        <linearGradient id="meeting" x1="0" y1="0" x2="1" y2="1">
          <stop offset="0" stop-color="#e6e6e6"/>
          <stop offset=".55" stop-color="#6d6f78"/>
          <stop offset="1" stop-color="#2c2e36"/>
        </linearGradient>
      </defs>
      <path d="M0 0 V552" stroke="var(--grey-mid)" stroke-width="14"/>
      <path d="M60 118 H390 V318 C300 300 170 320 26 372 C44 292 52 200 60 118 Z" fill="url(#meeting)" role="img" aria-label="Photo: two businessmen in discussion at a meeting table"/>
      <path d="M60 118 C52 200 44 292 26 372" fill="none" stroke="var(--blue)" stroke-width="6"/>
      <path d="M26 372 C170 320 300 300 390 318" fill="none" stroke="var(--blue)" stroke-width="3"/>
      <path d="M26 372 C18 420 14 480 14 552" fill="none" stroke="var(--blue)" stroke-width="6"/>
      <rect x="30" y="462" width="346" height="64" fill="var(--blue)"/>
    </svg>
    <div class="abs cover-brand"><span class="brand-name">Tavesi and Durando</span></div>
    <h1 class="abs cover-title">
      <span class="dark">Claims</span><br>
      <span class="accent">Management</span><br>
      <span class="dark">Company</span>
    </h1>
    <p class="abs cover-strap">trusted by clients worldwide to deliver the best in claims management, loss adjusting and auditing services to pre-risk and damage surveying</p>
  </article>
</section>

<section class="spread inner-spread">
  <article class="page who-we-are">
    <svg viewBox="0 0 390 552" aria-hidden="true">
      <defs>
        <linearGradient id="workdesk" x1="0" y1="0" x2="1" y2="1">
          <stop offset="0" stop-color="#3a4c66"/>
          <stop offset=".6" stop-color="#8a8f96"/>
          <stop offset="1" stop-color="#c9ccd0"/>
        </linearGradient>
      </defs>
      <path d="M330 0 Q380 60 372 160 Q370 200 390 230 V0 Z" fill="var(--grey-mid)"/>
      <path d="M350 0 Q392 70 384 170 Q384 200 390 210 V0 Z" fill="var(--blue)"/>
      <path d="M0 292 Q200 222 390 248" fill="none" stroke="var(--blue)" stroke-width="8"/>
      <path d="M0 300 Q200 232 390 256 V552 H0 Z" fill="url(#workdesk)" role="img" aria-label="Photo: man working at a computer showing an insurance claim form"/>
    </svg>
    <h2 class="abs section-head who-head">Who we are</h2>
    <p class="abs body-copy who-copy-1">We are a network of loss adjusters and technical experts working alongside insurers and brokers. Since our founding we have handled complex claims with care, speed and clear reporting, supporting every step from the first notice of loss to the final settlement.</p>
    <p class="abs body-copy who-copy-2">Each company in our group focuses on a specific field, from property and liability to renewable energy and technology risks. This shared structure lets us combine local presence with specialist knowledge, so clients receive one point of contact and a consistent standard of service across the country.</p>
  </article>

  <article class="page company-profile">
    <svg viewBox="0 0 390 552" aria-hidden="true">
      <defs>
        <linearGradient id="flatlay" x1="0" y1="0" x2="1" y2="1">
          <stop offset="0" stop-color="#fafafa"/>
          <stop offset="1" stop-color="#dcdcdc"/>
        </linearGradient>
        <linearGradient id="inspection" x1="0" y1="0" x2="1" y2="1">
          <stop offset="0" stop-color="#8f2a25"/>
          <stop offset=".6" stop-color="#4a2a26"/>
          <stop offset="1" stop-color="#cfc4bb"/>
        </linearGradient>
      </defs>
      <rect x="0" y="0" width="390" height="240" fill="url(#flatlay)" role="img" aria-label="Photo: desk with claim form clipboard, glasses, coffee cup and plant"/>
      <path d="M0 228 C120 176 260 186 390 206" fill="none" stroke="var(--grey-mid)" stroke-width="5"/>
      <path d="M0 238 C120 188 260 196 390 214 V552 H0 Z" fill="var(--blue)"/>
      <path d="M222 236 H390 V404 H222 Q204 404 204 386 V254 Q204 236 222 236 Z" fill="url(#inspection)" stroke="#fff" stroke-width="3" role="img" aria-label="Photo: adjuster inspecting damage on a red car and taking notes"/>
    </svg>
    <h2 class="abs profile-title">Company<br>Profile</h2>
    <p class="abs body-copy profile-copy">Our adjusters operate throughout the territory with fast site inspections, accurate damage assessment and transparent reports. We manage claims of every size, offering insurers a reliable partner for surveys, auditing and risk evaluation.</p>
    <h2 class="abs section-head why-head">Why do we use it?</h2>
    <p class="abs body-copy why-copy">Insurers choose us because we combine technical depth with practical experience. Our teams use modern tools, from drone surveys to thermographic analysis, to reach a fair outcome quickly. Every file follows a clear process, with regular updates for the client and a complete, well documented final report.</p>
  </article>
</section>

</body>
</html>
```